FlintHollow Blog Needs a New Look!
Past The Ridge - blog layout!
Thankyou Flinthollow Team :-)
Thank you to EACH of you for submitting some amazing designs. The choice was hard and we hope you all know how much we appreciate all that you have done!
Good luck on all future projects,
The FH Team
Good luck and congratz for the winner!
cheer!
Thanks for all of your hard work everyone! We will be announcing the winner early next week. Enjoy your weekend :)
Thanks for all of the great designs so far!
That is correct, no coding is needed - only design. We have someone in house that will flip the design into the correct code for us.
The dimensions will be for a typical QuillPage blog. We can always adjust later.
We have asked for NO logos in this contest - any of these designs have been eliminated.
Also, we have eliminated designs that look almost identical to other drafts that may have been submitted (by the same designer). Please only submit different drafts. If it's a background color change, we can change that at finalization.
Lastly, NO bubbled or heavy designs. The tabs should NOT resemble a bubbly/round look. Please abide by a sleek, classic design.
Thanks!
I'm in! What are the dimensions for the layout? Thanks!
@ "Only design. That's all these contest require, no coding comes with design. Thanks!"
So, we just design what it should look like and you guy do the coding yourself to make it look like what we design? Sorry for the question, I'm a bit confused.
Hello everyone, a few things we'd like to highlight.
Please omit the top banner ad.
Reduce the amount of tabs at top to include ONLY "about us" "archive" "contact" "FlintHollow"
Rework the header. We would like the logo on the left, then on the right we'd like chatterly, peepster, reeltube buttons with a search bar underneath.
Concentrate on sleek, clean design. No bubbly, heavy designs please.
#27 & #28 we've eliminated your designs. This is a blog design contest, not a logo contest.
Hello everyone,
We've decided to extend the contest! We've chosen our new logo and we have a little bit of a different approach to take.
Please consider and use the following:
-Rework the header. We would like the logo (which will be reattached to this project) on the left, then on the right we'd like chatterly, peepster, reeltube buttons with a search bar underneath.
- Concentrate on sleek, clean design. No bubbly, heavy designs please.
- The blog posts should be on the left, with a side bar. But, the side bar should be smaller than where the blog posts sit.
- Please try the tabs above to be in a row - these should include "about us" "archive" "contact" "FlintHollow"
Thanks! We are interested to see what you'll come up with!
-The FH Team
Can we try without the banner at top? Thanks!
We're liking what we see! Could we see a few with only tabs for "home" "FlintHollow" & "contact us?"
Also #7 could we try a few lighter colors? the grey is a bit drab.
Thanks!!
Thanks for all the great submissions! We are putting the contest on hold, just for about a day or two - we are working on a new brand/logo for our blog. Once this is updated we will relaunch! We'll let you know as soon as this happens!
Only design. That's all these contest require, no coding comes with design. Thanks!
You need a template with the design idea or the code?

```html
<!DOCTYPE html>
<html lang="en">
<head>
<meta charset="utf-8">
<title>FlintHollow Blog Layout</title>
<link href="https://fonts.googleapis.com/css2?family=Arimo:wght@400;700&display=swap" rel="stylesheet">
<style>
:root{
  --frame:#0c0c0c;
  --backdrop:#d4d4d4;
  --page:#ffffff;
  --ink:#1f1f1f;
  --muted:#8a8a8a;
  --teal:#2aa9c9;
  --teal-dark:#1d8fae;
  --lime:#a8c72a;
  --lime-light:#c4dc52;
  --lime-pale:#d5e77e;
  --red:#d62a1e;
  --nav:#151515;
  --panel:#e6e6e6;
  --panel-line:#c9c9c9;
}
*{margin:0;padding:0;box-sizing:border-box}
html,body{width:1200px;height:925px;overflow:hidden;background:#fff;font-family:"Arimo",Arial,sans-serif;color:var(--ink)}
.canvas{position:relative;width:1200px;height:925px;background:#fff}
.frame{position:absolute;left:70px;top:55px;width:1060px;height:815px;background:var(--frame)}
.backdrop{position:absolute;left:120px;top:0;width:960px;height:815px;background:linear-gradient(90deg,#2a2a2a 0%,var(--backdrop) 7%,var(--backdrop) 93%,#2a2a2a 100%)}
.page{position:absolute;left:120px;top:0;width:820px;height:815px;background:var(--page);left:120px}
.abs{position:absolute}

.brand{left:225px;top:88px;color:var(--teal);font-size:38px;font-weight:700;letter-spacing:-1px}
.slogan{left:300px;top:133px;color:var(--muted);font-size:9px}

.nav{left:527px;top:102px;display:flex;gap:5px}
.nav a{display:block;background:var(--nav);color:#fff;font-size:10px;font-weight:700;text-decoration:none;padding:5px 9px;height:20px;border-top:2px solid #555}

.search{left:742px;top:162px;width:253px;height:30px;background:#bdbdbd;display:flex;align-items:center}
.search .icon{width:30px;height:30px;background:#9a9a9a;display:flex;align-items:center;justify-content:center}
.search span{color:#fff;font-size:12px;margin-left:10px}
.sidebar{left:742px;top:192px;width:253px;height:520px;background:linear-gradient(180deg,#f2f2f2,#ffffff 30%)}

.datebox{width:40px;height:52px;background:#333;color:#fff;text-align:center}
.datebox b{display:block;font-size:17px;line-height:20px;padding-top:3px}
.datebox small{display:block;font-size:8px}
.datebox i{display:block;background:var(--red);font-style:normal;font-size:7px;margin-top:3px;padding:1px 0}
.post-title{font-size:20px;font-weight:700}
.meta{font-size:8px;color:var(--muted)}
.meta em{color:var(--teal);font-style:normal}
.comments{width:72px;height:18px;background:var(--teal);color:#fff;font-size:8px;font-weight:700;text-align:center;line-height:18px;border-radius:3px 3px 0 0}
.card{width:513px;height:213px;background:linear-gradient(180deg,var(--lime-light),var(--lime));border-radius:0 0 40px 0}
.thumb{position:absolute;left:30px;top:35px;width:163px;height:163px;background:var(--lime-pale);display:flex;align-items:center;justify-content:center;color:#fff;font-size:14px}
.excerpt{position:absolute;left:208px;top:28px;width:280px;color:#fff;font-size:9px;line-height:13px}
.more{position:absolute;right:28px;bottom:18px;color:#fff;font-size:17px}

.links{left:782px;top:262px;width:193px}
.links li{list-style:none;position:relative;height:26px;margin-bottom:3px;background:var(--teal);color:#fff;font-size:13px;font-weight:700;line-height:26px;padding-left:12px}
.links li::before{content:"";position:absolute;left:-32px;top:0;width:26px;height:26px;background:#c2c2c2}

.top-tab{left:767px;top:465px;width:113px;height:25px;background:var(--red);color:#fff;font-size:13px;font-weight:700;line-height:25px;text-align:center}
.top-list{left:742px;top:495px;width:240px;background:var(--panel);padding:8px 12px}
.top-list li{list-style:none;font-size:8px;color:#333;height:32px;line-height:32px;border-bottom:1px solid var(--panel-line)}
.top-list li:last-child{border-bottom:0}
</style>
</head>
<body>
<div class="canvas">
  <div class="frame">
    <div class="backdrop"></div>
  </div>
  <div class="page abs" style="left:190px;top:55px;width:820px;height:815px"></div>

  <div class="abs brand">FlintHollow</div>
  <div class="abs slogan">Slogan</div>

  <nav class="abs nav">
    <a>HOME</a><a>START A PROJECT</a><a>FIND A PROJECT</a><a>HOW IT WORKS</a><a>CONTACT US</a>
  </nav>

  <div class="abs sidebar"></div>
  <div class="abs search">
    <div class="icon"><svg width="14" height="14" viewBox="0 0 14 14"><circle cx="6" cy="6" r="4" fill="none" stroke="#fff" stroke-width="2"/><line x1="9" y1="9" x2="13" y2="13" stroke="#fff" stroke-width="2"/></svg></div>
    <span>Search</span>
  </div>

  <!-- post one -->
  <div class="abs datebox" style="left:230px;top:207px"><b>6</b><small>tweets</small><i>tweet</i></div>
  <h2 class="abs post-title" style="left:283px;top:213px">Where is your phone book?</h2>
  <div class="abs meta" style="left:283px;top:240px">Tuesday 12 January 2012 | <em>Marla Ketterby</em></div>
  <div class="abs comments" style="left:620px;top:259px">7 Comments</div>
  <article class="abs card" style="left:232px;top:277px">
    <div class="thumb" role="img" aria-label="Post image placeholder">picture</div>
    <p class="excerpt">I'm not exactly sure where I have to ask this, but our team keeps debating it. Every time a directory arrives at my door, I wonder if anyone still flips through those pages. Most of the numbers I need live on my phone now, yet the books keep piling up by the entrance. Perhaps local shops still rely on them, or perhaps the habit simply refuses to fade away.</p>
    <span class="more">Read more ▸</span>
  </article>

  <!-- post two -->
  <div class="abs datebox" style="left:230px;top:520px"><b>75</b><small>tweets</small><i>tweet</i></div>
  <h2 class="abs post-title" style="left:283px;top:537px">New Upgrades For Designers!</h2>
  <div class="abs meta" style="left:283px;top:564px">Tuesday 5 January 2012 | <em>Marla Ketterby</em></div>
  <div class="abs comments" style="left:620px;top:589px">15 Comments</div>
  <article class="abs card" style="left:232px;top:607px">
    <div class="thumb" role="img" aria-label="Post image placeholder">picture</div>
    <p class="excerpt">We released the first part of our big announcement earlier this week on our designer page. Part one covered how designers will now be able to receive donations from project holders. This update lets designers showcase the work they are proud of and helps new clients find them. Holders who want to thank a designer can now do so directly.</p>
    <span class="more">Read more ▸</span>
  </article>

  <ul class="abs links">
    <li>FlintHollow Forums</li>
    <li>Follow Us</li>
    <li>Become a Fan</li>
    <li>Subscribe to RSS</li>
    <li>FH Edu Channel</li>
  </ul>

  <ul class="abs top-list">
    <li>How to Lose a Design Contest in 10 Ways</li>
    <li>7 Habits of Successful Graphic Designers</li>
    <li>The 10 Commandments for New Designers</li>
    <li>Help! I Suffer from Designer's Block</li>
    <li>How to Handle Your Client's Criticism Positively</li>
    <li>Launch a Design Contest in Less than 10 Minutes</li>
  </ul>
  <div class="abs top-tab">Our Top Posts</div>
</div>
</body>
</html>
```